Verdant Solutions Business Card

want the back of card to be blue- with the logo in the center
front of card- info plus logo (info being mailing address, email address, and website address )
4 different names with titles to have on cards
1) Dalton Mirsky - Owner
2) Brenda Tolvin- Customer Relationship Specialist
3) Henri Kastner- Vice President of Sales
4) Wade Dunmor- Chief Technology Officer

Target Market(s)

tech company in the government/probation office industry

Industry/Entity Type

Government Office

Contact Information for Business Card

1) Dalton Mirsky - Owner

Colors
0355a3
ffffff

Requirements
Must have
• back side should be blue, with the logo placed in the center
• front side needs to include both the logo, as well as company info (info should include website address, email address, and mailing address)

```html
<!DOCTYPE html>
<html lang="en">
<head>
<meta charset="utf-8">
<title>Verdant Solutions Business Card</title>
<link rel="stylesheet" href="https://fonts.googleapis.com/css2?family=Cinzel:wght@500;600&family=Roboto:wght@400&display=swap">
<style>
  :root {
    --page-bg: #e4e2de;
    --card-bg: #f4f3f0;
    --navy: #1f2f5c;
    --ink-gray: #5b6068;
    --line-gray: #6c7077;
  }
  * { box-sizing: border-box; margin: 0; padding: 0; }
  html, body { width: 1200px; height: 1054px; overflow: hidden; }
  body { background: var(--page-bg); position: relative; font-family: "Roboto", Arial, sans-serif; }
  .card {
    position: absolute; left: 100px; top: 227px; width: 1000px; height: 600px;
    background: var(--card-bg); overflow: hidden;
    box-shadow: 0 10px 30px rgba(0,0,0,.12);
  }
  .brand-name {
    position: absolute; left: 38px; top: 58px;
    font-family: "Cinzel", Georgia, serif; font-weight: 600;
    font-size: 46px; line-height: 1.02; color: var(--navy); letter-spacing: 1px;
  }
  .edge-tab { position: absolute; left: 0; top: 265px; }
  .holder-name {
    position: absolute; left: 38px; top: 272px;
    font-family: "Cinzel", Georgia, serif; font-weight: 500;
    font-size: 34px; color: var(--navy); letter-spacing: 1px;
  }
  .holder-title {
    position: absolute; left: 38px; top: 325px;
    font-size: 24px; color: var(--ink-gray);
  }
  .contact-list { position: absolute; left: 38px; top: 410px; list-style: none; }
  .contact-item {
    display: flex; align-items: center; height: 38px;
    font-size: 25px; color: var(--ink-gray);
  }
  .contact-icon { width: 22px; height: 22px; margin-right: 29px; flex: none; }
  .mail-address {
    position: absolute; left: 38px; top: 532px;
    font-size: 25px; color: var(--ink-gray);
  }
  .mark-circle { position: absolute; left: 560px; top: 70px; }
</style>
</head>
<body>
  <section class="card" aria-label="Business card front">
    <div class="brand-name">Verdant<br>Solutions</div>

    <svg class="mark-circle" width="460" height="460" viewBox="0 0 460 460" aria-hidden="true">
      <circle cx="230" cy="230" r="215" fill="none" stroke="var(--navy)" stroke-width="14"/>
    </svg>

    <svg class="edge-tab" width="18" height="110" viewBox="0 0 18 110" aria-hidden="true">
      <path d="M0 0 A18 55 0 0 1 0 110 Z" fill="var(--navy)"/>
    </svg>

    <h1 class="holder-name">Brenda Tolvin</h1>
    <p class="holder-title">Customer Relationship Specialist</p>

    <ul class="contact-list">
      <li class="contact-item">
        <svg class="contact-icon" viewBox="0 0 24 24" aria-hidden="true">
          <path d="M3 8c0-3 4-4 9-4s9 1 9 4v2h-5V8H8v2H3z" fill="var(--line-gray)"/>
          <path d="M6 12h12l2 8H4z" fill="var(--line-gray)"/>
          <circle cx="12" cy="16" r="2.2" fill="var(--card-bg)"/>
        </svg>
        555-014-2290
      </li>
      <li class="contact-item">
        <svg class="contact-icon" viewBox="0 0 24 24" aria-hidden="true">
          <rect x="2" y="5" width="20" height="14" fill="var(--line-gray)"/>
          <path d="M2.5 5.5 12 13l9.5-7.5" fill="none" stroke="var(--card-bg)" stroke-width="1.6"/>
        </svg>
        brenda.t@verdantsolutions.com
      </li>
      <li class="contact-item">
        <svg class="contact-icon" viewBox="0 0 24 24" aria-hidden="true">
          <circle cx="12" cy="12" r="10" fill="var(--line-gray)"/>
          <g fill="none" stroke="var(--card-bg)" stroke-width="1.3">
            <ellipse cx="12" cy="12" rx="4.5" ry="10"/>
            <path d="M2 12h20M4 7h16M4 17h16M12 2v20"/>
          </g>
        </svg>
        www.verdantsolutions.com
      </li>
    </ul>

    <p class="mail-address">810 Fenwick Ave., Linden Falls, US 48213</p>
  </section>
</body>
</html>
```